"contact us" Flyer for Marketing Drop-offs

We need a simple 3rd of a page (3 3/4" x 8 1/2") flyer made for quick customer interaction.

These should display our logo, tagline, and our contact information. The background should incorporate the attached picture/color scheme.

This flyer will be offering an incentive to be determined at a later date.

Industry/Entity Type

Legal

Font styles to use
Serif
Sans Serif

Colors
0255a3
33a6d7
876aae

Requirements
Must have
• proper color scheme, simple/modern layout, attached logo
Nice to have
• creativity with working, placement
Should not have
• extra/meaningless characters, shapes

```html
<!DOCTYPE html>
<html lang="en">
<head>
<meta charset="utf-8">
<title>Lone Range Records – Contact Flyer</title>
<link rel="stylesheet" href="https://fonts.googleapis.com/css2?family=Cabin:wght@500;700&display=swap">
<style>
  :root {
    --stage: #e9e7e3;
    --navy-deep: #1f2d5e;
    --navy: #2c3d78;
    --navy-soft: #3d4f8c;
    --ink-light: #ffffff;
  }
  * { box-sizing: border-box; margin: 0; padding: 0; }
  html, body {
    width: 1200px;
    height: 1000px;
    overflow: hidden;
    background: var(--stage);
  }
  .flyer {
    position: absolute;
    left: 336px;
    top: 0;
    width: 528px;
    height: 1000px;
    overflow: hidden;
    color: var(--ink-light);
    font-family: "Cabin", sans-serif;
  }
  .flyer__backdrop {
    position: absolute;
    inset: 0;
    background:
      radial-gradient(ellipse at 30% 20%, var(--navy-soft) 0%, transparent 55%),
      radial-gradient(ellipse at 75% 70%, var(--navy-soft) 0%, transparent 50%),
      linear-gradient(160deg, var(--navy) 0%, var(--navy-deep) 50%, var(--navy) 100%);
  }
  .brand {
    position: absolute;
    top: 200px;
    left: 0;
    width: 100%;
    display: flex;
    align-items: center;
    justify-content: center;
    gap: 16px;
  }
  .brand__mark {
    width: 22px;
    height: 22px;
    background: var(--ink-light);
  }
  .brand__name {
    font-weight: 700;
    font-size: 52px;
    line-height: 1.1;
    text-align: center;
    width: 380px;
  }
  .divider {
    position: absolute;
    top: 414px;
    left: 100px;
    width: 326px;
    height: 4px;
    background: var(--ink-light);
  }
  .tagline {
    position: absolute;
    top: 476px;
    left: 0;
    width: 100%;
    text-align: center;
    font-weight: 500;
    font-size: 23px;
    line-height: 37.5px;
  }
  .contact {
    position: absolute;
    left: 108px;
    top: 730px;
    list-style: none;
  }
  .contact__item {
    display: flex;
    align-items: center;
    height: 46px;
    margin-bottom: 31px;
    font-size: 22px;
    font-weight: 500;
  }
  .contact__icon {
    width: 50px;
    height: 46px;
    margin-right: 18px;
    display: flex;
    align-items: center;
    justify-content: center;
  }
  .contact__icon svg { fill: var(--ink-light); }
</style>
</head>
<body>
  <main class="flyer">
    <div class="flyer__backdrop" role="img" aria-label="Marbled navy blue swirl background"></div>

    <div class="brand">
      <span class="brand__mark"></span>
      <span class="brand__name">Lone Range Records</span>
    </div>

    <div class="divider"></div>

    <p class="tagline">
      ... is the premier source for<br>
      Country Clerk Records and<br>
      Mineral Appraisal Data covering<br>
      Texas, Oklahoma,<br>
      New Mexico and Colorado
    </p>

    <ul class="contact">
      <li class="contact__item">
        <span class="contact__icon">
          <svg width="48" height="34" viewBox="0 0 48 34" aria-hidden="true">
            <path d="M0 0h48v34H0z M3 3v1l21 15L45 4V3z M3 7v24h42V7L24 22z" fill-rule="evenodd"/>
          </svg>
        </span>
        youremail@mail.com
      </li>
      <li class="contact__item">
        <span class="contact__icon">
          <svg width="46" height="46" viewBox="0 0 24 24" aria-hidden="true">
            <path d="M6.6 10.8a15.1 15.1 0 0 0 6.6 6.6l2.2-2.2c.3-.3.7-.4 1-.2 1.1.4 2.3.6 3.6.6.6 0 1 .4 1 1V20c0 .6-.4 1-1 1A17 17 0 0 1 3 4c0-.6.4-1 1-1h3.5c.6 0 1 .4 1 1 0 1.3.2 2.5.6 3.6.1.3 0 .7-.2 1z"/>
          </svg>
        </span>
        0123456789
      </li>
      <li class="contact__item">
        <span class="contact__icon">
          <svg width="34" height="48" viewBox="0 0 24 34" aria-hidden="true">
            <path d="M12 0A12 12 0 0 0 0 12c0 9 12 22 12 22s12-13 12-22A12 12 0 0 0 12 0zm0 17a5 5 0 1 1 0-10 5 5 0 0 1 0 10z"/>
          </svg>
        </span>
        Street address, zip
      </li>
    </ul>
  </main>
</body>
</html>
```